Create Web Design Template with Source Files

I need a web design built with PSD/source files. See attached design I have made to guidance. Also I have attached an image I have used so you can use it.

I got my inspiration from this site if you would like to use it also:
http://trelvix.com/home

PSD & html slicing and responsive designs also. So we can run across all devices.

Number of Pages Required

1 page

Requirements
Must have
• See attachments. Ask if you have any questions...

```html
<!DOCTYPE html>
<html lang="en">
<head>
<meta charset="utf-8">
<title>Voxa — The Modern Debate and Opinion</title>
<link href="https://fonts.googleapis.com/css2?family=Montserrat:wght@600;700;800&family=Open+Sans:wght@400;600;700&display=swap" rel="stylesheet">
<style>
:root{
  --purple:#8e0aa8;
  --ink:#1e1e1e;
  --text:#333;
  --muted:#666;
  --rule:#cfcfcf;
  --white:#fff;
}
*{box-sizing:border-box;margin:0;padding:0}
html,body{width:1200px;height:3141px;overflow:hidden;background:var(--white);font-family:"Open Sans",Arial,sans-serif;color:var(--text)}
.page{position:relative;width:1200px;height:3141px;overflow:hidden}

.site-header{position:absolute;top:0;left:0;width:1200px;height:86px;background:var(--white);border-bottom:1px solid #e6e6e6}
.brand{position:absolute;left:70px;top:16px;font-family:"Montserrat",sans-serif;font-weight:800;font-size:44px;line-height:50px;color:var(--purple)}
.search{position:absolute;left:613px;top:26px;width:323px;height:36px;border-bottom:1px solid #bbb;font-size:14px;color:#555;line-height:34px}
.search svg{position:absolute;right:2px;top:8px}
.login{position:absolute;left:993px;top:21px;width:104px;height:44px;border:2px solid var(--purple);border-radius:22px;color:var(--purple);font-family:"Montserrat",sans-serif;font-weight:700;font-size:15px;display:flex;align-items:center;justify-content:center;gap:6px}

.sidebar{position:absolute;top:86px;left:0;width:281px;height:3055px;background:linear-gradient(180deg,#1a1a1a,#0c0c0c 60%,#151515)}
.side-nav{list-style:none}
.side-nav li{position:absolute;left:37px;display:flex;align-items:center;gap:14px;font-family:"Montserrat",sans-serif;font-weight:600;font-size:14px;color:var(--white);text-transform:uppercase;white-space:nowrap}
.side-nav li.active{color:var(--purple)}
.social{position:absolute;left:0;width:281px;top:2932px;text-align:center}
.social h4{font-family:"Montserrat",sans-serif;font-weight:600;font-size:17px;color:var(--white);letter-spacing:1px}
.social-links{display:flex;justify-content:center;gap:12px;margin-top:30px}
.social-links span{width:42px;height:42px;border:2px solid var(--white);border-radius:50%}

.hero{position:absolute;left:281px;top:86px;width:919px;height:459px;background:linear-gradient(160deg,#5b4a44 0%,#3a2f2c 45%,#1c1818 100%)}
.hero h1{position:absolute;left:41px;top:298px;font-family:"Montserrat",sans-serif;font-weight:700;font-size:45px;line-height:56px;color:var(--white);text-transform:uppercase}

.content{position:absolute;left:324px;top:545px;width:777px}
.section{margin-top:45px}
.section+.section{margin-top:61px}
.section-head{height:65px;border-bottom:1px solid var(--rule);position:relative}
.section-head h2{position:absolute;left:0;top:6px;font-family:"Montserrat",sans-serif;font-weight:700;font-size:30px;line-height:32px;color:var(--ink);text-transform:uppercase}
.subscribe{position:absolute;top:0;height:42px;width:141px;border-radius:21px;background:var(--purple);color:var(--white);font-family:"Montserrat",sans-serif;font-weight:700;font-size:14px;display:flex;align-items:center;justify-content:center;gap:7px;text-transform:uppercase}
.subscribe.with-arrows{left:513px}
.subscribe.solo{right:0}
.arrow{position:absolute;top:1px;width:40px;height:40px;border:1px solid #999;border-radius:50%;display:flex;align-items:center;justify-content:center}
.arrow.prev{left:688px}.arrow.next{left:736px}

.cards{display:flex;gap:18px;margin-top:44px}
.card{width:247px}
.card-image{height:189px;border:3px solid #e3e3e3;box-shadow:0 1px 3px rgba(0,0,0,.2)}
.card-title{margin-top:22px;font-weight:600;font-size:15.5px;line-height:25px;color:var(--ink);white-space:nowrap;letter-spacing:-.1px}
.card-meta{margin-top:16px;height:37px;border-bottom:1px solid var(--rule);font-size:13px;color:var(--muted);display:flex;align-items:flex-start;gap:6px;line-height:20px}
.card-meta svg{margin-top:4px}
.card-meta .sep{margin:0 4px}
.author{margin-top:17px;display:flex;align-items:center;gap:18px;font-size:16px;color:var(--ink)}
.avatar{width:70px;height:70px;border-radius:50%;background:#d9d9d9;border:3px solid #bdbdbd}

.categories{display:grid;grid-template-columns:repeat(3,247px);column-gap:18px;row-gap:21px;margin-top:44px}
.category{height:237px;border:2px solid #e0e0e0;box-shadow:0 1px 3px rgba(0,0,0,.18)}
.category-image{height:185px}
.category-name{height:48px;display:flex;align-items:center;justify-content:center;font-weight:600;font-size:20px;color:var(--ink);white-space:nowrap}
.view-more{display:flex;align-items:center;justify-content:center;width:142px;height:46px;margin:38px auto 0;border:2px solid var(--purple);border-radius:23px;color:var(--purple);font-family:"Montserrat",sans-serif;font-weight:700;font-size:15px;text-transform:uppercase}
.site-footer{margin-top:54px;border-top:1px solid var(--rule);padding-top:40px;text-align:center;font-size:13px;color:var(--muted)}
</style>
</head>
<body>
<div class="page">
  <header class="site-header">
    <div class="brand">VOXA</div>
    <div class="search">Search
      <svg width="18" height="18" viewBox="0 0 18 18"><circle cx="7.5" cy="7.5" r="5.5" fill="none" stroke="#333" stroke-width="2.2"/><path d="M11.5 11.5l5 5" stroke="#333" stroke-width="2.6" stroke-linecap="round"/></svg>
    </div>
    <div class="login"><svg width="12" height="14" viewBox="0 0 12 14"><path d="M3 6V4a3 3 0 016 0v2" fill="none" stroke="#8e0aa8" stroke-width="2"/><rect x="1" y="6" width="10" height="8" rx="1" fill="#8e0aa8"/></svg>LOGIN</div>
  </header>

  <aside class="sidebar">
    <ul class="side-nav">
      <li class="active" style="top:84px"><svg width="22" height="18" viewBox="0 0 22 18"><path d="M11 1L1 9h3v8h5v-5h4v5h5V9h3z" fill="#8e0aa8"/></svg>Home</li>
      <li style="top:165px"><svg width="20" height="20" viewBox="0 0 20 20"><circle cx="10" cy="10" r="10" fill="#fff"/><text x="10" y="15" text-anchor="middle" font-family="Arial" font-weight="700" font-size="14" fill="#111">?</text></svg>How it works</li>
      <li style="top:245px"><svg width="20" height="20" viewBox="0 0 20 20"><circle cx="10" cy="10" r="10" fill="#fff"/><rect x="8.5" y="8" width="3" height="8" fill="#111"/><circle cx="10" cy="5" r="1.7" fill="#111"/></svg>About us</li>
      <li style="top:325px"><svg width="24" height="20" viewBox="0 0 24 20"><ellipse cx="12" cy="8.5" rx="11" ry="7.5" fill="#fff"/><path d="M5 13l-2 6 7-4z" fill="#fff"/></svg>Weapons of comments</li>
    </ul>
    <div class="social">
      <h4>SOCIAL</h4>
      <div class="social-links"><span></span><span></span><span></span><span></span></div>
    </div>
  </aside>

  <section class="hero" role="img" aria-label="Cheering crowd of young people at a live event">
    <h1>The Modern<br>Debate and Opinion</h1>
  </section>

  <main class="content">
    <section class="section">
      <div class="section-head"><h2>Featured</h2>
        <span class="subscribe with-arrows"><svg width="11" height="13" viewBox="0 0 11 13"><path d="M1 0h9v13l-4.5-3.5L1 13z" fill="#fff"/></svg>Subscribe</span>
        <span class="arrow prev"><svg width="10" height="14" viewBox="0 0 10 14"><path d="M8 1L2 7l6 6" fill="none" stroke="#333" stroke-width="1.6"/></svg></span>
        <span class="arrow next"><svg width="10" height="14" viewBox="0 0 10 14"><path d="M2 1l6 6-6 6" fill="none" stroke="#333" stroke-width="1.6"/></svg></span>
      </div>
      <div class="cards">
        <article class="card"><div class="card-image" role="img" aria-label="Speaker at a conference panel table" style="background:linear-gradient(135deg,#4a4f66,#2b2a30 60%,#8a7a6a)"></div><h3 class="card-title">Nemo enim ipsa voluplstatem<br>quia voluptas sit..</h3><div class="card-meta"><svg width="11" height="12" viewBox="0 0 11 12"><rect x="0" y="1.5" width="11" height="10.5" rx="1" fill="#8e0aa8"/><rect x="1.5" y="4.5" width="8" height="6" fill="#fff"/></svg>1 day ago<span class="sep">|</span><svg width="11" height="11" viewBox="0 0 11 11"><path d="M0 0h5l6 6-5 5-6-6z" fill="#8e0aa8"/><circle cx="2.5" cy="2.5" r="1" fill="#fff"/></svg>Opinion</div><div class="author"><span class="avatar"></span>Lena Varkov</div></article>
        <article class="card"><div class="card-image" role="img" aria-label="Man speaking into a microphone at a meeting" style="background:linear-gradient(135deg,#d9dde3,#5a6380 55%,#2a2c36)"></div><h3 class="card-title">Nemo enim ipsa voluplstatem<br>quia voluptas sit..</h3><div class="card-meta"><svg width="11" height="12" viewBox="0 0 11 12"><rect x="0" y="1.5" width="11" height="10.5" rx="1" fill="#8e0aa8"/><rect x="1.5" y="4.5" width="8" height="6" fill="#fff"/></svg>1 day ago<span class="sep">|</span><svg width="11" height="11" viewBox="0 0 11 11"><path d="M0 0h5l6 6-5 5-6-6z" fill="#8e0aa8"/><circle cx="2.5" cy="2.5" r="1" fill="#fff"/></svg>Debate</div><div class="author"><span class="avatar"></span>Lena Varkov</div></article>
        <article class="card"><div class="card-image" role="img" aria-label="People talking in a bright modern lounge" style="background:linear-gradient(135deg,#9fc6e6,#3f7fb8 50%,#c9c36a)"></div><h3 class="card-title">Nemo enim ipsa voluplstatem<br>quia voluptas sit..</h3><div class="card-meta"><svg width="11" height="12" viewBox="0 0 11 12"><rect x="0" y="1.5" width="11" height="10.5" rx="1" fill="#8e0aa8"/><rect x="1.5" y="4.5" width="8" height="6" fill="#fff"/></svg>1 day ago<span class="sep">|</span><svg width="11" height="11" viewBox="0 0 11 11"><path d="M0 0h5l6 6-5 5-6-6z" fill="#8e0aa8"/><circle cx="2.5" cy="2.5" r="1" fill="#fff"/></svg>Opinion</div><div class="author"><span class="avatar"></span>Lena Varkov</div></article>
      </div>
    </section>

    <section class="section">
      <div class="section-head"><h2>Trending</h2>
        <span class="subscribe with-arrows"><svg width="11" height="13" viewBox="0 0 11 13"><path d="M1 0h9v13l-4.5-3.5L1 13z" fill="#fff"/></svg>Subscribe</span>
        <span class="arrow prev"><svg width="10" height="14" viewBox="0 0 10 14"><path d="M8 1L2 7l6 6" fill="none" stroke="#333" stroke-width="1.6"/></svg></span>
        <span class="arrow next"><svg width="10" height="14" viewBox="0 0 10 14"><path d="M2 1l6 6-6 6" fill="none" stroke="#333" stroke-width="1.6"/></svg></span>
      </div>
      <div class="cards">
        <article class="card"><div class="card-image" role="img" aria-label="Two athletes lifting barbells in a gym" style="background:linear-gradient(135deg,#3a3a3a,#6b5a4e 55%,#2a2a2a)"></div><h3 class="card-title">Nemo enim ipsa voluplstatem<br>quia voluptas sit..</h3><div class="card-meta"><svg width="11" height="12" viewBox="0 0 11 12"><rect x="0" y="1.5" width="11" height="10.5" rx="1" fill="#8e0aa8"/><rect x="1.5" y="4.5" width="8" height="6" fill="#fff"/></svg>1 day ago<span class="sep">|</span><svg width="11" height="11" viewBox="0 0 11 11"><path d="M0 0h5l6 6-5 5-6-6z" fill="#8e0aa8"/><circle cx="2.5" cy="2.5" r="1" fill="#fff"/></svg>Debate</div><div class="author"><span class="avatar"></span>Lena Varkov</div></article>
        <article class="card"><div class="card-image" role="img" aria-label="Paraglider over a turquoise sea coast" style="background:linear-gradient(180deg,#6fb8d8,#1f7f9e 55%,#6b6040)"></div><h3 class="card-title">Nemo enim ipsa voluplstatem<br>quia voluptas sit..</h3><div class="card-meta"><svg width="11" height="12" viewBox="0 0 11 12"><rect x="0" y="1.5" width="11" height="10.5" rx="1" fill="#8e0aa8"/><rect x="1.5" y="4.5" width="8" height="6" fill="#fff"/></svg>1 day ago<span class="sep">|</span><svg width="11" height="11" viewBox="0 0 11 11"><path d="M0 0h5l6 6-5 5-6-6z" fill="#8e0aa8"/><circle cx="2.5" cy="2.5" r="1" fill="#fff"/></svg>Debate</div><div class="author"><span class="avatar"></span>Lena Varkov</div></article>
        <article class="card"><div class="card-image" role="img" aria-label="Surfer riding a large blue wave" style="background:linear-gradient(135deg,#0b5f8a,#2fb1c9 55%,#d7eef2)"></div><h3 class="card-title">Nemo enim ipsa voluplstatem<br>quia voluptas sit..</h3><div class="card-meta"><svg width="11" height="12" viewBox="0 0 11 12"><rect x="0" y="1.5" width="11" height="10.5" rx="1" fill="#8e0aa8"/><rect x="1.5" y="4.5" width="8" height="6" fill="#fff"/></svg>1 day ago<span class="sep">|</span><svg width="11" height="11" viewBox="0 0 11 11"><path d="M0 0h5l6 6-5 5-6-6z" fill="#8e0aa8"/><circle cx="2.5" cy="2.5" r="1" fill="#fff"/></svg>Opinion</div><div class="author"><span class="avatar"></span>Lena Varkov</div></article>
      </div>
    </section>

    <section class="section">
      <div class="section-head"><h2>Daily Humor</h2>
        <span class="subscribe with-arrows"><svg width="11" height="13" viewBox="0 0 11 13"><path d="M1 0h9v13l-4.5-3.5L1 13z" fill="#fff"/></svg>Subscribe</span>
        <span class="arrow prev"><svg width="10" height="14" viewBox="0 0 10 14"><path d="M8 1L2 7l6 6" fill="none" stroke="#333" stroke-width="1.6"/></svg></span>
        <span class="arrow next"><svg width="10" height="14" viewBox="0 0 10 14"><path d="M2 1l6 6-6 6" fill="none" stroke="#333" stroke-width="1.6"/></svg></span>
      </div>
      <div class="cards">
        <article class="card"><div class="card-image" role="img" aria-label="Child hugging a golden dog" style="background:linear-gradient(135deg,#4f7a3a,#c08a4a 55%,#d23a2a)"></div><h3 class="card-title">Nemo enim ipsa voluplstatem<br>quia voluptas sit..</h3><div class="card-meta"><svg width="11" height="12" viewBox="0 0 11 12"><rect x="0" y="1.5" width="11" height="10.5" rx="1" fill="#8e0aa8"/><rect x="1.5" y="4.5" width="8" height="6" fill="#fff"/></svg>1 day ago<span class="sep">|</span><svg width="11" height="11" viewBox="0 0 11 11"><path d="M0 0h5l6 6-5 5-6-6z" fill="#8e0aa8"/><circle cx="2.5" cy="2.5" r="1" fill="#fff"/></svg>Opinion</div><div class="author"><span class="avatar"></span>Lena Varkov</div></article>
        <article class="card"><div class="card-image" role="img" aria-label="Glowing telephone handset sketch on a dark board" style="background:linear-gradient(135deg,#1d2a3a,#2c4a5c 55%,#14202c)"></div><h3 class="card-title">Nemo enim ipsa voluplstatem<br>quia voluptas sit..</h3><div class="card-meta"><svg width="11" height="12" viewBox="0 0 11 12"><rect x="0" y="1.5" width="11" height="10.5" rx="1" fill="#8e0aa8"/><rect x="1.5" y="4.5" width="8" height="6" fill="#fff"/></svg>1 day ago<span class="sep">|</span><svg width="11" height="11" viewBox="0 0 11 11"><path d="M0 0h5l6 6-5 5-6-6z" fill="#8e0aa8"/><circle cx="2.5" cy="2.5" r="1" fill="#fff"/></svg>Debate</div><div class="author"><span class="avatar"></span>Lena Varkov</div></article>
        <article class="card"><div class="card-image" role="img" aria-label="Young green sprouts growing in soil" style="background:linear-gradient(180deg,#9fcf6a,#3f7a22 50%,#1c2a12)"></div><h3 class="card-title">Nemo enim ipsa voluplstatem<br>quia voluptas sit..</h3><div class="card-meta"><svg width="11" height="12" viewBox="0 0 11 12"><rect x="0" y="1.5" width="11" height="10.5" rx="1" fill="#8e0aa8"/><rect x="1.5" y="4.5" width="8" height="6" fill="#fff"/></svg>1 day ago<span class="sep">|</span><svg width="11" height="11" viewBox="0 0 11 11"><path d="M0 0h5l6 6-5 5-6-6z" fill="#8e0aa8"/><circle cx="2.5" cy="2.5" r="1" fill="#fff"/></svg>Opinion</div><div class="author"><span class="avatar"></span>Lena Varkov</div></article>
      </div>
    </section>

    <section class="section">
      <div class="section-head"><h2>Categories</h2>
        <span class="subscribe solo"><svg width="11" height="13" viewBox="0 0 11 13"><path d="M1 0h9v13l-4.5-3.5L1 13z" fill="#fff"/></svg>Subscribe</span>
      </div>
      <div class="categories">
        <div class="category"><div class="category-image" role="img" aria-label="Couple cycling in a green park" style="background:linear-gradient(135deg,#6a9a4a,#3b6e9a 55%,#8ab06a)"></div><div class="category-name">Healthy Living</div></div>
        <div class="category"><div class="category-image" role="img" aria-label="Red and gold festival lanterns" style="background:linear-gradient(135deg,#c8201a,#e0a020 55%,#8a1010)"></div><div class="category-name">Culture</div></div>
        <div class="category"><div class="category-image" role="img" aria-label="Woman holding a black leather handbag" style="background:linear-gradient(135deg,#e8d8d0,#b07a6a 50%,#1a1a1a)"></div><div class="category-name">Fashion</div></div>
        <div class="category"><div class="category-image" role="img" aria-label="Microphones held out toward a politician" style="background:linear-gradient(135deg,#5a6a80,#2a2a34 55%,#8a8a8a)"></div><div class="category-name">Politics</div></div>
        <div class="category"><div class="category-image" role="img" aria-label="Close-up of an eye with digital interface" style="background:linear-gradient(135deg,#0e2a40,#2f8ab8 55%,#0a1a28)"></div><div class="category-name">Science &amp; Technology</div></div>
        <div class="category"><div class="category-image" role="img" aria-label="Racing car on a track" style="background:linear-gradient(180deg,#e8ecef,#9aa4ac 60%,#5a5f64)"></div><div class="category-name">Sports</div></div>
      </div>
      <a class="view-more">View More</a>
    </section>

    <footer class="site-footer">Copyrights © 2018, Voxa. All rights reserved.</footer>
  </main>
</div>
</body>
</html>
```